Jewelry Shop Needs a Business Card Design

***We want a very sharp and unforgettable pantone for the Business Card. ***
***We do not want the business card or logo only in black, white and grey color!!!Please provide us a main color as our brand topic! Thanks!! ***

Mabel’s Nook is a Hong Kong based fine jewelry brand.

We want a very nice, simple and elegant business card design for Mabel's Nook Brand. The company's logo has been uploaded already.

You can design with below info:

Desmond Yip
Director
M: +852 94726305
T: +852 35842947
F: +852 35842949
E: desmond.yip@mabelsnook.example
9/F , Harbourlight Tower, 18-24 Fenwick Lane, Sai Wan Ho, Kowloon, Hong Kong

Target Market(s)

Mabel’s Nook philosophy is a jewelry icon of young, creative, trendy, fashionable, stylish, energetic, and elegant. For Mabel’s Nook, jewelry is one collection of artworks, the most important items in personal life.

Industry/Entity Type

Jewelry

Requirements
Must have
• We want a very sharp and unforgettable pantone for the Business Card.

```html
<!DOCTYPE html>
<html lang="en">
<head>
<meta charset="utf-8">
<title>Mabel’s Nook — Business Card</title>
<link rel="stylesheet" href="https://fonts.googleapis.com/css2?family=Cinzel:wght@400&family=Jost:wght@400;600&display=swap">
<style>
  :root {
    --backdrop: #958b8e;
    --card: #dcdcdc;
    --ink: #2b2b2b;
    --ink-soft: #3c3c3c;
    --brand: #00727a;
  }
  * { margin: 0; padding: 0; box-sizing: border-box; }
  html, body { width: 1200px; height: 1091px; overflow: hidden; }
  body {
    background: var(--backdrop);
    position: relative;
    font-family: "Jost", "Futura", sans-serif;
    color: var(--ink);
  }
  .card {
    position: absolute;
    top: 262px;
    width: 340px;
    height: 566px;
    background: var(--card);
  }
  .card--back { left: 170px; }
  .card--front { left: 690px; }

  /* Front */
  .brand-disc {
    position: absolute;
    left: 91px;
    top: 108px;
    width: 158px;
    height: 158px;
    border-radius: 50%;
    background: var(--brand);
  }
  .brand-name {
    position: absolute;
    left: 0;
    right: 0;
    top: 318px;
    text-align: center;
    font-family: "Cinzel", "Trajan Pro", serif;
    font-size: 22px;
    letter-spacing: 0.06em;
    color: var(--brand);
  }

  /* Back */
  .contact {
    position: absolute;
    left: 0;
    right: 0;
    top: 218px;
    text-align: center;
  }
  .contact__name {
    font-weight: 600;
    font-size: 19px;
    letter-spacing: 0.12em;
    text-transform: uppercase;
    color: var(--brand);
  }
  .contact__role {
    margin-top: 6px;
    font-size: 10px;
    letter-spacing: 0.2em;
    text-transform: uppercase;
    color: var(--ink-soft);
  }
  .rule {
    width: 30px;
    height: 2px;
    background: var(--brand);
    margin: 14px auto;
  }
  .phones {
    list-style: none;
    display: inline-block;
    text-align: left;
    font-size: 15px;
    letter-spacing: 0.16em;
    line-height: 23px;
  }
  .phones span { display: inline-block; width: 22px; font-size: 13px; }
  .contact__email {
    margin-top: 6px;
    font-size: 10px;
    letter-spacing: 0.06em;
    text-transform: uppercase;
  }
  .contact__address {
    font-style: normal;
    font-size: 10.5px;
    letter-spacing: 0.08em;
    line-height: 27px;
    text-transform: uppercase;
    color: var(--ink-soft);
  }
</style>
</head>
<body>
  <section class="card card--back" aria-label="Business card, contact side">
    <div class="contact">
      <h1 class="contact__name">Desmond Yip</h1>
      <p class="contact__role">Director</p>
      <div class="rule"></div>
      <ul class="phones">
        <li><span>m.</span>+852 94726305</li>
        <li><span>t.</span>+852 35842947</li>
        <li><span>f.</span>+852 35842949</li>
      </ul>
      <p class="contact__email">desmond.yip@mabelsnook.example</p>
      <div class="rule"></div>
      <address class="contact__address">
        9/F , Harbourlight Tower, 18-24<br>
        Fenwick Lane, Sai Wan Ho,<br>
        Kowloon, Hong Kong
      </address>
    </div>
  </section>

  <section class="card card--front" aria-label="Business card, brand side">
    <div class="brand-disc"></div>
    <p class="brand-name">Mabel’s Nook</p>
  </section>
</body>
</html>
```